Willow Bloom Services Business Card Design

I require a business card design for my business Willow Bloom Services. The purpose of this business is to enable people to make positive change in their lives. This business offers life coaching, hypnotherapy and facilitation services. The slogan is 'Rise from the ashes and live the life you want.' Coaching services will be available internationally whilst the hypnotherapy and facilitation services will focus on delivery in south east Queensland.

The business card should be crisp, clean, professional and give the client positive feelings of achieving success.

The logo must be representative of a Willow Bloom from the ashes which is a symbol of regeneration and new life. My preference is a black Phoenix on a white background similar to the Phoenix image attached to this brief. I'm happy to see other concepts you have too. The logo and business name must be scalable so it can be printed on a large outdoor sign. Therefore the following files must be provided as a minimum:
-Business card
-Logo on it's own
-Business name on it's own

The following detail must appear on either the front/back of the business card
-Logo
-Willow Bloom Services
-Rise from the ashes and live the life you want.
-Personal and business success through
-Coaching | Hypnotherapy | Facilitation
-Della Harcourt
-Founder

-Life Coach
-Clinical Hypnotherapist
-MBA (Project Management specialisation)
-Neuro Linguistic Programming Practitioner

-0418 372 906
-E: willowbloom.au@mailhaven.com
-www.willow-bloom.com.au
-Contact us now for your free 20min assessment

Please feel free to ask me as many questions as you like :) Thank you.

Hi all,  friendly reminder that the logo needs to be your own design and cannot be a Imagequarry or other purchased or free image.  

Thanks heaps
Keep the great designs coming in. You're all so talented.
Della

• Feedback from older people is that black backgrounds with lighter fonts are difficult to read so please no black backgrounds.

```html
<!DOCTYPE html>
<html lang="en">
<head>
<meta charset="utf-8">
<title>Willow Bloom Services – Business Card</title>
<link rel="stylesheet" href="https://fonts.googleapis.com/css2?family=Open+Sans:wght@400;600;700&family=Montserrat:wght@500;600&display=swap">
<style>
  :root {
    --backdrop: #e4e4e2;
    --card: #fbfbfa;
    --ink: #1d1d1d;
    --orange: #e8620f;
    --orange-soft: #f29a4a;
    --red: #d3252b;
    --feather: rgba(170, 170, 170, 0.16);
  }
  * { margin: 0; padding: 0; box-sizing: border-box; }
  html, body { width: 1200px; height: 1200px; overflow: hidden; }
  body {
    background: var(--backdrop);
    font-family: "Open Sans", Arial, sans-serif;
    color: var(--ink);
    position: relative;
  }
  .card {
    position: absolute;
    left: 322px;
    width: 556px;
    height: 346px;
    background: var(--card);
    overflow: hidden;
  }
  .card--front { top: 204px; }
  .card--back { top: 672px; }

  .feather-art {
    position: absolute;
    top: 0;
    right: 0;
    width: 130px;
    height: 100%;
    background: linear-gradient(200deg, var(--feather), rgba(170,170,170,0.04) 75%, transparent);
  }

  .front__title {
    position: absolute;
    left: 34px;
    top: 40px;
    font-weight: 700;
    font-size: 16px;
    letter-spacing: 1.2px;
    color: var(--orange);
  }
  .front__list {
    position: absolute;
    left: 34px;
    top: 74px;
    list-style: none;
    font-size: 13px;
    letter-spacing: 1.3px;
    line-height: 17.4px;
  }
  .front__list--gap { margin-top: 17.4px; }
  .front__cta {
    position: absolute;
    left: 0;
    top: 283px;
    width: 100%;
    height: 30px;
    background: var(--orange);
    color: #fff;
    font-weight: 700;
    font-size: 14px;
    letter-spacing: 1.6px;
    line-height: 30px;
    padding-left: 34px;
  }

  .brand {
    position: absolute;
    left: 30px;
    top: 41px;
    display: flex;
    align-items: center;
    gap: 14px;
  }
  .brand__dot {
    width: 70px;
    height: 70px;
    border-radius: 50%;
    background: var(--orange);
  }
  .brand__name {
    font-family: "Montserrat", Arial, sans-serif;
    font-weight: 500;
    font-size: 36px;
    color: var(--ink);
  }
  .person {
    position: absolute;
    right: 30px;
    top: 172px;
    text-align: right;
  }
  .person__name {
    font-family: "Montserrat", Arial, sans-serif;
    font-weight: 600;
    font-size: 20px;
    letter-spacing: 0.5px;
  }
  .person__role {
    margin-top: 8px;
    font-size: 14px;
    letter-spacing: 2.6px;
    color: var(--red);
  }
  .contact {
    position: absolute;
    left: 30px;
    top: 256px;
    list-style: none;
    font-size: 15.5px;
    letter-spacing: 1.5px;
    line-height: 24px;
  }
  .contact__label {
    color: var(--red);
    font-weight: 700;
    display: inline-block;
    width: 28px;
  }
</style>
</head>
<body>
  <section class="card card--front">
    <div class="feather-art" role="img" aria-label="Faint line drawing of trailing feathers"></div>
    <h1 class="front__title">Willow Bloom Services</h1>
    <ul class="front__list">
      <li>-Willow Bloom Services</li>
      <li>-Rise from the ashes and live the life you want</li>
      <li>-Personal and business success through</li>
      <li>-Coaching | Hypnotherapy | Facilitation</li>
      <li>-Della Harcourt</li>
      <li>-Founder</li>
      <li class="front__list--gap">-Life Coach</li>
      <li>-Clinical Hypnotherapist</li>
      <li>-MBA (Project Management specialisation)</li>
      <li>-Neuro Linguistic Programming Practitioner</li>
    </ul>
    <p class="front__cta">CONTACT US NOW FOR YOUR FREE 20MIN ASSESSMENT</p>
  </section>

  <section class="card card--back">
    <div class="feather-art" role="img" aria-label="Faint line drawing of trailing feathers"></div>
    <div class="brand">
      <span class="brand__dot"></span>
      <span class="brand__name">Willow Bloom</span>
    </div>
    <div class="person">
      <p class="person__name">DELLA HARCOURT</p>
      <p class="person__role">DIRECTOR</p>
    </div>
    <ul class="contact">
      <li><span class="contact__label">M.</span>0418 372 906</li>
      <li><span class="contact__label">E.</span>WILLOWBLOOM.AU@MAILHAVEN.COM</li>
      <li><span class="contact__label">W.</span>WWW.WILLOWBLOOM.COM.AU</li>
    </ul>
  </section>
</body>
</html>
```